Poster for homelessness project (2 day deadline)

Amber Lantern Scheme is an initiative in the UK which aims to ensure that people who are new to sleeping on the street are quickly given assistance to take them out of situation they find themselves in.

It began as a London-based project but is now being rolled out nationwide. I am working for a project based in the north of England.

We need some posters which show an image of a place where a rough sleeper may spend the night with some supporting graphic design.

I have three initial images, but I need to be able to easily swap out the images for others. I would appreciate if you could produce three posters for me, each with a different image.

-
Please note:
My client is quite vague about what they want at the moment and the above words may change. I need the selected product to be a layered raw file that I can amend myself with any Adobe CS5.5 (or below) application.

Any typefaces that you choose need to be easily purchasable online.

Please view formatinfo.pdf for formatting guidelines.

Target Market(s)

The general public. It will be placed in public places.

Industry/Entity Type

Graphic Design

Requirements
Must have
• Must contain the words:

"Tonight someone will sleep rough for the first time. Help us make sure they find the Amber Lantern."

"Would you sleep here? Sleeping rough is dangerous. Make sure everyone finds the Amber Lantern."

-
Nice to have
• I'd like this to be quite bleak, grimy and "urban" in feel.

You may recolour/tint the images in any way to enhance this feeling.

```html
<!DOCTYPE html>
<html lang="en">
<head>
<meta charset="utf-8">
<title>Amber Lantern Scheme – Tonight Someone Will Sleep Rough</title>
<link rel="stylesheet" href="https://fonts.googleapis.com/css2?family=Cabin+Sketch:wght@700&family=Londrina+Sketch&family=Kaushan+Script&family=Oswald:wght@400;500&display=swap">
<style>
  :root {
    --ink-black: #111010;
    --chalk-white: #f4efe6;
    --rust-red: #8a2a17;
    --ember: #b8472a;
    --iron-grey: #9c948a;
    --soot: #2a1a14;
    --sand: #c9a27c;
  }
  * { margin: 0; padding: 0; box-sizing: border-box; }
  html, body {
    width: 1200px;
    height: 849px;
    overflow: hidden;
    background: var(--soot);
  }
  .poster {
    position: relative;
    width: 1200px;
    height: 849px;
    overflow: hidden;
  }
  .scene-photo {
    position: absolute;
    inset: 0;
    background:
      radial-gradient(ellipse 420px 320px at 1120px 60px, rgba(30,18,12,0.85), transparent 70%),
      radial-gradient(ellipse 520px 300px at 960px 520px, rgba(200,60,40,0.55), transparent 70%),
      linear-gradient(100deg, #b7afa4 0%, #a79c8e 30%, #9a7a62 50%, #7d3a26 72%, #5a2316 100%);
  }
  .scene-photo::after {
    content: "";
    position: absolute;
    inset: 0;
    background: linear-gradient(180deg, transparent 0%, transparent 45%, rgba(110,35,20,0.75) 80%, rgba(80,22,12,0.9) 100%);
  }
  .headline {
    position: absolute;
    left: 14px;
    top: 40px;
    font-family: "Cabin Sketch", cursive;
    font-weight: 700;
    font-size: 236px;
    line-height: 1;
    letter-spacing: -6px;
    color: var(--ink-black);
    text-transform: uppercase;
    transform: scaleX(0.88);
    transform-origin: left top;
  }
  .subject {
    position: absolute;
    left: 66px;
    top: 258px;
    font-family: "Londrina Sketch", cursive;
    font-size: 124px;
    line-height: 1;
    letter-spacing: -2px;
    color: var(--chalk-white);
    text-transform: uppercase;
  }
  .tagline {
    position: absolute;
    left: 52px;
    top: 382px;
    font-family: "Kaushan Script", cursive;
    font-size: 44px;
    line-height: 1.2;
    color: var(--chalk-white);
    white-space: nowrap;
  }
  .tagline .emphasis { font-size: 66px; }
  .appeal {
    position: absolute;
    left: 0;
    right: 0;
    top: 718px;
    text-align: center;
    font-family: "Oswald", sans-serif;
    font-weight: 500;
    font-size: 33px;
    color: var(--chalk-white);
  }
  .question {
    position: absolute;
    left: 0;
    right: 0;
    top: 785px;
    text-align: center;
    font-family: "Oswald", sans-serif;
    font-weight: 400;
    font-size: 21px;
    color: var(--sand);
  }
</style>
</head>
<body>
  <main class="poster">
    <div class="scene-photo" role="img" aria-label="Grimy photograph of a corrugated metal wall, concrete steps and a red park bench under a tree, tinted rust red"></div>

    <h1 class="headline">Tonight</h1>
    <p class="subject">Someone</p>
    <p class="tagline">will sleep rough for the <span class="emphasis">first</span> time.</p>

    <p class="appeal">Help us make sure they find the Amber Lantern</p>
    <p class="question">Would you sleep here? Sleeping rough is dangerous. Make sure everyone finds the Amber Lantern.</p>
  </main>
</body>
</html>
```